We are a new company with 2 divisions a medical research and medical product sales. We need a company logo and Business Cards. The design files need to be provided to us in Adobe Photoshop CS 5.1.

Target Market(s)

Medical Community

Industry/Entity Type

Medical

Contact Information for Business Card

Company Name - Larkmoor Biomedical LLC
Company Address 4217 NE 14th Ave Suite 7, Gainesville Fl 32609

Requirements
Must have
• The design files need to be provided to us in Adobe Photoshop CS 5.1.

```html
<!DOCTYPE html>
<html lang="en">
<head>
<meta charset="utf-8">
<title>Larkmoor Biomedical LLC – Business Cards</title>
<link href="https://fonts.googleapis.com/css2?family=Open+Sans:wght@400;600;700&display=swap" rel="stylesheet">
<style>
  :root {
    --stage-top: #e9e9e9;
    --stage-bottom: #a9a9a9;
    --brand-blue: #1f6fc2;
    --deep-blue: #0c4f8f;
    --navy: #0a3768;
    --sky-blue: #5aa6e4;
    --brand-red: #d8232a;
    --dark-red: #8f1a1f;
    --ink: #3c3c3c;
    --paper: #ffffff;
  }
  * { box-sizing: border-box; margin: 0; padding: 0; }
  html, body { width: 1200px; height: 900px; overflow: hidden; }
  body {
    background: linear-gradient(180deg, var(--stage-top) 0%, #d2d2d2 55%, var(--stage-bottom) 100%);
    font-family: "Open Sans", sans-serif;
    position: relative;
  }
  .card {
    position: absolute;
    top: 295px;
    width: 520px;
    height: 300px;
    border-radius: 22px;
    overflow: hidden;
    box-shadow: 0 10px 24px rgba(0,0,0,0.25);
  }
  /* Back of card */
  .card--back { left: 50px; }
  .back-pattern {
    position: absolute; inset: 0;
    background:
      radial-gradient(ellipse 38% 55% at 92% 30%, rgba(120,185,240,0.55), transparent 70%),
      radial-gradient(ellipse 30% 40% at 85% 85%, rgba(110,175,235,0.45), transparent 70%),
      linear-gradient(100deg, var(--navy) 0%, var(--deep-blue) 40%, var(--brand-blue) 75%, var(--sky-blue) 100%);
  }
  .back-brand {
    position: absolute;
    left: 0; right: 0; top: 118px;
    text-align: center;
    color: var(--paper);
    font-weight: 700;
  }
  .back-brand__name { font-size: 44px; letter-spacing: -1px; line-height: 1; }
  .back-brand__suffix { font-size: 11px; letter-spacing: 6px; margin-top: 6px; }
  .back-brand__dot {
    width: 46px; height: 46px; border-radius: 50%;
    background: var(--paper);
    position: absolute; left: 237px; top: -68px;
  }

  /* Front of card */
  .card--front { left: 630px; background: var(--paper); }
  .front-brand {
    position: absolute; left: 36px; top: 34px;
    display: flex; align-items: center; gap: 16px;
    color: var(--brand-blue); font-weight: 700;
  }
  .front-brand__dot {
    width: 66px; height: 66px; border-radius: 50%;
    background: var(--brand-blue);
  }
  .front-brand__name { font-size: 38px; letter-spacing: -1px; line-height: 1; }
  .front-brand__suffix { font-size: 10px; letter-spacing: 5px; margin-top: 4px; }
  .person { position: absolute; left: 36px; top: 124px; }
  .person__name { color: var(--brand-blue); font-size: 18px; font-weight: 600; line-height: 24px; }
  .person__title { color: var(--ink); font-size: 13px; line-height: 18px; }
  .contacts {
    position: absolute; left: 36px; top: 176px;
    list-style: none; color: var(--ink); font-size: 13px; line-height: 18px;
  }
  .contacts li { display: flex; align-items: flex-start; gap: 5px; }
  .contacts svg { width: 14px; height: 14px; flex: none; margin-top: 2px; fill: var(--brand-blue); }
  .contacts .indent { padding-left: 19px; }
  .swoosh { position: absolute; left: 0; bottom: 0; width: 520px; height: 110px; }
</style>
</head>
<body>

<section class="card card--back" aria-label="Card back">
  <div class="back-pattern" role="img" aria-label="Blue background with a receding pattern of overlapping light-blue ovals"></div>
  <div class="back-brand">
    <div class="back-brand__dot"></div>
    <div class="back-brand__name">Larkmoor</div>
    <div class="back-brand__suffix">BIOMEDICAL LLC</div>
  </div>
</section>

<section class="card card--front" aria-label="Card front">
  <div class="front-brand">
    <div class="front-brand__dot"></div>
    <div>
      <div class="front-brand__name">Larkmoor</div>
      <div class="front-brand__suffix">BIOMEDICAL LLC</div>
    </div>
  </div>

  <div class="person">
    <div class="person__name">Dr. Elena Whitcombe</div>
    <div class="person__title">Managing Director</div>
  </div>

  <ul class="contacts">
    <li><svg viewBox="0 0 16 16"><path d="M3 1l3 3-1.5 2a9 9 0 0 0 5.5 5.5L12 10l3 3-2 2C7 15 1 9 1 3z"/></svg>323-555-0148</li>
    <li><svg viewBox="0 0 16 16"><path d="M4 1h8v14H4zM5.5 3v7h5V3z"/></svg>323-555-0172</li>
    <li><svg viewBox="0 0 16 16"><circle cx="8" cy="8" r="7" fill="none" stroke="#1f6fc2" stroke-width="1.5"/><path d="M1 8h14M8 1v14" stroke="#1f6fc2" stroke-width="1.2"/></svg>www.larkmoorbio.com</li>
    <li><svg viewBox="0 0 16 16"><path d="M8 1l7 7h-2v7H9.5v-4h-3v4H3V8H1z"/></svg>4217 NE 14th Ave Suite 7,</li>
    <li class="indent">Gainesville Fl 32609</li>
  </ul>

  <svg class="swoosh" viewBox="0 0 520 110" preserveAspectRatio="none" aria-hidden="true">
    <path d="M0 84 C120 92 250 84 380 50 C450 32 490 26 520 24 L520 31 C490 33 450 39 380 57 C250 91 120 99 0 91 Z" fill="var(--brand-red)"/>
    <path d="M0 94 C120 102 250 94 380 61 C450 43 490 37 520 35 L520 39 C490 41 450 47 380 65 C250 98 120 106 0 98 Z" fill="var(--dark-red)" opacity="0.8"/>
    <path d="M0 98 C120 106 250 98 380 65 C450 47 490 41 520 39 L520 110 L0 110 Z" fill="var(--brand-blue)"/>
  </svg>
</section>

</body>
</html>
```